Bref créative
Brochure for Geriatric Clinic
LumaCrest Residence & Geriatric SPA
Trifold (3 panel) brochure to be designed for a healthcare company specialized in assisted living facilities and geriatric rehabilitation.
We want to see the medical, the infrastructure and the nature rich enviroment aspects of our business in the design.
We want the brochure to communicate that our primary goal is to improve the quality of life for the senior and their families.
Specification of the folder
11" x 8.5"
279.4 mm x 215.9 mm
27.9 cm x 21.6 cm
3.7" x 8.5"
93.0 mm x 215.9 mm
9.3 cm x 21.6 cm
Please refer to our website at www.lumacrest-care.example, we provided a google translate menu at the bottom for the designers convenience. All pictures are free to use in this project.
Health
Personal, elderly, seniors an their families
Lumacrest logo
.ai format
LumaCrest document brief for brochure

```html
<!DOCTYPE html>
<html lang="en">
<head>
<meta charset="utf-8">
<title>LumaCrest Residence &amp; Geriatric SPA – Brochure Interior</title>
<link rel="stylesheet" href="https://fonts.googleapis.com/css2?family=Cinzel:wght@700&family=EB+Garamond:ital,wght@0,400;0,600;1,400&family=Dancing+Script:wght@500&display=swap">
<style>
  :root {
    --stage: #e4e0d6;
    --paper: #d9d1ac;
    --paper-inner: #ece6cf;
    --frame: #b8ad7c;
    --heading: #6e6a36;
    --ink: #4d4a2c;
    --photo-border: #ffffff;
  }
  * { margin: 0; padding: 0; box-sizing: border-box; }
  html, body { width: 1200px; height: 799px; overflow: hidden; }
  body {
    background: var(--stage);
    font-family: "EB Garamond", Georgia, serif;
    color: var(--ink);
    position: relative;
  }
  .brochure {
    position: absolute; left: 30px; top: 50px;
    width: 1140px; height: 700px;
    display: flex;
    background: var(--paper);
    box-shadow: 0 4px 14px rgba(0,0,0,.18);
  }
  .panel {
    position: relative; width: 380px; height: 100%;
    padding: 16px;
    border-right: 1px solid rgba(0,0,0,.08);
  }
  .panel:last-child { border-right: none; }
  .panel-inner {
    position: relative; width: 100%; height: 100%;
    background: var(--paper-inner);
    border: 2px solid var(--frame);
    outline: 1px solid var(--photo-border);
    outline-offset: -6px;
    padding: 22px 24px;
  }
  .section-title {
    font-family: "Cinzel", serif; font-weight: 700;
    color: var(--heading); font-size: 17px; letter-spacing: .5px;
    margin-bottom: 8px;
  }
  .sub-title {
    font-family: "Cinzel", serif; font-weight: 700;
    color: var(--heading); font-size: 13px; margin-bottom: 4px;
  }
  .philosophy-text {
    font-family: "Dancing Script", cursive; font-size: 18px;
    line-height: 1.3; color: var(--heading);
  }
  .signature {
    font-family: "Dancing Script", cursive; font-size: 19px;
    color: var(--heading); margin: 10px 0 20px;
  }
  .service-list { list-style: decimal inside; font-size: 14px; line-height: 1.45; }
  .plain-list { list-style: none; font-size: 14px; line-height: 1.45; margin-bottom: 14px; }
  .plain-list li::before { content: "– "; color: var(--heading); }
  .body-text { font-size: 14px; line-height: 1.4; margin-bottom: 10px; }
  .photo {
    position: absolute; border: 5px solid var(--photo-border);
    box-shadow: 0 2px 6px rgba(0,0,0,.25);
  }
  .photo-room { left: 20px; top: 22px; width: 200px; height: 120px;
    background: linear-gradient(135deg, #eef0ee, #b9c2c0 60%, #8d9790); }
  .photo-lounge { left: 200px; top: 60px; width: 130px; height: 95px;
    background: linear-gradient(160deg, #cfd6d2, #7c8a7e); }
  .photo-pool { right: 22px; top: 22px; width: 200px; height: 95px;
    background: linear-gradient(180deg, #7fb3dc, #d8d1b4 55%, #4aa0c6); }
  .photo-garden { left: 22px; top: 70px; width: 140px; height: 100px;
    background: linear-gradient(180deg, #9ec7e4, #5f8d4a 55%, #3e6a33); }
  .photo-doctors { right: 22px; bottom: 26px; width: 210px; height: 125px;
    background: linear-gradient(135deg, #eef1f2, #c3ccd1 55%, #7e8d96); }
  .middle-text { position: absolute; left: 24px; right: 24px; top: 175px; }
  .right-text { position: absolute; left: 24px; right: 24px; top: 195px; }
</style>
</head>
<body>
  <main class="brochure">
    <section class="panel panel-left">
      <div class="panel-inner">
        <h2 class="section-title">OUR PHILOSOPHY</h2>
        <p class="philosophy-text">Our residence was founded on a simple belief: every senior deserves comfort, dignity and care. We combine modern medicine with warmth, nature and a true sense of home.</p>
        <p class="signature">Dr. Tobias Kwandel &amp;<br>Dr. Mara Kwandel</p>
        <h2 class="section-title">OUR SERVICES</h2>
        <h3 class="sub-title">NURSING HOME</h3>
        <ol class="service-list">
          <li>24-hour nursing care and supervision</li>
          <li>Individual care plans for each resident</li>
          <li>Rehabilitation and physiotherapy</li>
          <li>Medication management</li>
          <li>Balanced meals by our dietitians</li>
          <li>Social and cultural activities</li>
          <li>Wheelchair accessible rooms</li>
          <li>Dementia and Alzheimer's support</li>
          <li>Palliative and respite care</li>
          <li>Visits by specialists on request</li>
          <li>Weekly medical check-ups</li>
          <li>Wireless internet</li>
        </ol>
      </div>
    </section>

    <section class="panel panel-middle">
      <div class="panel-inner">
        <div class="photo photo-room" role="img" aria-label="Bright resident room with care bed"></div>
        <div class="photo photo-lounge" role="img" aria-label="Residence lounge interior"></div>
        <div class="middle-text">
          <h2 class="section-title">DAY CARE</h2>
          <p class="body-text">Seniors who live at home can join us for the day, sharing meals, therapy and activities with our residents while families rest assured.</p>
          <ul class="plain-list">
            <li>Assistance with daily needs</li>
            <li>Meals and afternoon tea</li>
            <li>Group exercise and walks</li>
            <li>Transport on request</li>
          </ul>
          <h2 class="section-title">OPTIONAL SERVICES</h2>
          <ul class="plain-list">
            <li>Physiotherapy</li>
            <li>Occupational therapy</li>
            <li>Hairdresser and pedicure</li>
            <li>Private transport to appointments</li>
            <li>Accompaniment to hospital visits</li>
            <li>Laundry and ironing</li>
          </ul>
        </div>
      </div>
    </section>

    <section class="panel panel-right">
      <div class="panel-inner">
        <div class="photo photo-pool" role="img" aria-label="Residence building with swimming pool"></div>
        <div class="photo photo-garden" role="img" aria-label="Green garden with walking path"></div>
        <div class="right-text">
          <p class="body-text">Dr. Tobias Kwandel graduated from the Medical University in 1994 and specialised in internal medicine and gerontology.</p>
          <p class="body-text">Dr. Mara Kwandel, physiotherapist, holds a master in geriatric rehabilitation and leads our therapy team.</p>
        </div>
        <div class="photo photo-doctors" role="img" aria-label="The two founding doctors in the clinic"></div>
      </div>
    </section>
  </main>
</body>
</html>
```